Business Card and Letterhead Design for Public Accounting Firm

Business card and letterhead design for a CPA Firm located in Orange County, CA. We're looking for a modern and professional design utilizing our existing logo. We'd like a clean "less is more" look, but also something that catches the eye. We provide a high level of service to our clients. Open to single or double sided business cards.

Additional info: color numbers on logo
Blue :
R 0
G 83
B 125

#00537D

Silver :

R 154
G 154
B 154

#9A9A9A

Target Market(s)

Businesses and individuals

Industry/Entity Type

Accounting

Contact Information for Business Card

Moss Whitfield & Danby LLP - 4827 Larkspur Vale Road, Irvine, CA 92614 - (949)731-2864 - mwdaccts.example

Font styles to use
Serif
Sans Serif
Other font styles liked:
• See font file uploaded

Colors
0054AA
0677BA
7BADD7
CADEEF
E8F1F8

Requirements
Nice to have
• Possibly use the font file provided which matches our logo, but adjust to be not in all caps

```html
<!DOCTYPE html>
<html lang="en">
<head>
<meta charset="utf-8">
<title>Moss Whitfield &amp; Danby LLP — Business Card</title>
<link href="https://fonts.googleapis.com/css2?family=Cinzel:wght@400;700&family=Montserrat:wght@400;700&display=swap" rel="stylesheet">
<style>
  :root {
    --brand-blue: #21557a;
    --brand-silver: #9a9a9a;
    --card-white: #f7f7f7;
    --ink: #222222;
    --rule-grey: #b5b5b5;
    --page: #ececec;
  }
  * { box-sizing: border-box; margin: 0; padding: 0; }
  html, body { width: 1200px; height: 1145px; overflow: hidden; }
  body {
    background: var(--page);
    display: flex;
    flex-direction: column;
    align-items: center;
    justify-content: center;
    gap: 70px;
    font-family: "Montserrat", sans-serif;
  }
  .card {
    width: 630px;
    height: 360px;
    display: flex;
    align-items: center;
    box-shadow: 0 6px 18px rgba(0,0,0,0.12);
  }
  .card--front { background: var(--card-white); }
  .card--back { background: var(--brand-blue); }

  .card__mark {
    width: 300px;
    display: flex;
    justify-content: center;
  }
  .wordmark {
    font-family: "Cinzel", serif;
    font-weight: 700;
    font-size: 27px;
    line-height: 1.2;
    text-align: center;
    color: var(--brand-blue);
  }
  .card--back .wordmark { color: #ffffff; }

  .card__divider {
    width: 1px;
    height: 170px;
    background: var(--rule-grey);
  }
  .card--back .card__divider { background: #8aa3b7; }

  .card__details { padding-left: 36px; }
  .firm-heading {
    font-family: "Cinzel", serif;
    font-weight: 700;
    font-size: 24px;
    color: var(--brand-blue);
  }
  .rule {
    width: 110px;
    height: 1px;
    background: var(--brand-blue);
    margin: 12px 0 14px;
  }
  .contact-list { list-style: none; }
  .contact-list li {
    display: flex;
    align-items: center;
    gap: 10px;
    font-size: 15px;
    color: var(--ink);
    line-height: 1.55;
  }
  .contact-icon {
    width: 14px;
    height: 14px;
    flex: none;
  }
  .address {
    font-size: 15px;
    color: var(--ink);
    line-height: 1.45;
    font-style: normal;
  }
  .address strong { font-weight: 700; }

  .firm-name-full {
    padding-left: 30px;
    font-family: "Cinzel", serif;
    font-weight: 400;
    font-size: 24px;
    letter-spacing: 2px;
    line-height: 1.25;
    color: var(--brand-silver);
  }
</style>
</head>
<body>

  <section class="card card--front" aria-label="Business card front">
    <div class="card__mark">
      <p class="wordmark">Moss Whitfield<br>&amp; Danby</p>
    </div>
    <div class="card__divider"></div>
    <div class="card__details">
      <h1 class="firm-heading">Moss Whitfield</h1>
      <div class="rule"></div>
      <ul class="contact-list">
        <li>
          <svg class="contact-icon" viewBox="0 0 14 14" aria-hidden="true"><circle cx="7" cy="7" r="6.3" fill="none" stroke="#21557a" stroke-width="1"/><path d="M5 4.2 L6 5.6 L5.4 6.3 Q6.2 7.9 7.7 8.6 L8.4 8 L9.8 9 L9.3 10 Q6.5 10 4.2 5 Z" fill="#21557a"/></svg>
          (949) 731-2864
        </li>
        <li>
          <svg class="contact-icon" viewBox="0 0 14 14" aria-hidden="true"><circle cx="7" cy="7" r="6.3" fill="none" stroke="#21557a" stroke-width="1"/><rect x="4" y="5" width="6" height="4.2" fill="#21557a"/><path d="M4 5 L7 7.3 L10 5" fill="none" stroke="#fff" stroke-width="0.7"/></svg>
          office@mwdaccts.example
        </li>
        <li>
          <svg class="contact-icon" viewBox="0 0 14 14" aria-hidden="true"><circle cx="7" cy="7" r="6.3" fill="none" stroke="#21557a" stroke-width="1"/><circle cx="7" cy="7" r="3.4" fill="none" stroke="#21557a" stroke-width="0.8"/><path d="M3.6 7 H10.4 M7 3.6 V10.4" stroke="#21557a" stroke-width="0.7"/></svg>
          www.mwdaccts.example
        </li>
      </ul>
      <div class="rule"></div>
      <address class="address">
        4827 Larkspur Vale Road,<br>
        Irvine, <strong>CA 92614</strong>
      </address>
    </div>
  </section>

  <section class="card card--back" aria-label="Business card back">
    <div class="card__mark">
      <p class="wordmark">Moss Whitfield<br>&amp; Danby</p>
    </div>
    <div class="card__divider"></div>
    <p class="firm-name-full">Moss Whitfield<br>&amp; Danby LLP</p>
  </section>

</body>
</html>
```